Paper Lanterns - Borrowed Summers

I need an eBook cover.

The book is about changing the way we treat and teach our children. It exposes the truth about our children's unhappiness, and our misguided attempts at helping them, which is only causing more distress.

I map out how schooling the way we do, as well as hierarchical and controlling parenting methods, are not only outdated, they were never meant to bring out the best in our children. Each generation has been paying an ever-higher price for conforming. The current generation is falling apart, being injured by our willingness to medicate them rather than change the way we treat and teach them. But it is not only about medication, or medicated children - so I don't think medication on the cover would be right. An unhappy or frustrated child perhaps. I think that the cover needs to reflect the title, and the current rates of depression, and diagnoses that are the reality of today's childhood. With maybe something that shows a glimmer of hope.
Updates

Project Deadline Extended Reason: My first description and resulting designs made me realize that there weren't reflecting the title, and seemed confusing. I have extended the deadline and tried to identify key points that might better reflect what might be more congruent. I hope so!I have also committed to payment. Added Wednesday, October 12, 2016

Target Market(s)

All parents, extended families, educators, retired educators, teenagers.

Industry/Entity Type

Education

Requirements
Must have
• I will put my additional thought about the front cover in the Nice to Haves section because they are just thoughts and not must haves.
• Some minor wishes for the back cover - in case it makes a difference: I want the back cover to have a small picture of me and I will put a short bio next to it. The bottom half of the back I will probably get some endorsements of the book OR write a summary.
• I assume that I will be able to do these in the final cover - myself or with your help?
• I have included the logo that will be used as my Publishing Co logo. Just fyi.
Nice to have
• Just thinking here.
• A bored, or angry child looking out a classroom window at some nature, perhaps a natural courtyard with an oak tree. On the window sill - along with other typical classroom stuff, a Bonsai tree, like a class experiment. It should not be too noticeable, more subliminal. In the book I do compare the two tree types as an analogy (oak and bonsai). Across the way, maybe an office building with an adult also longingly looking out a window at the courtyard. lol -- is this too much? Maybe I need to have this scene photographed? Is it possible to overlay these things? Otherwise a drawing?
• In the colors I think I like the blues. Maybe part of the cover needs to be in Grayscale as a reflection of the child and adult's mood? Again, just thinking.

```html
<!DOCTYPE html>
<html lang="en">
<head>
<meta charset="utf-8">
<title>Paper Lanterns - Borrowed Summers — Book Cover</title>
<link href="https://fonts.googleapis.com/css2?family=Roboto+Condensed:wght@700&family=PT+Sans:wght@400;700&display=swap" rel="stylesheet">
<style>
  :root {
    --stage: #000000;
    --paper: #ffffff;
    --brand-red: #a51d2a;
    --swoosh-red: #e31b23;
    --swoosh-dark: #8e0f17;
    --ink: #000000;
    --body-ink: #1a1a1a;
    --bokeh-light: #b8472f;
    --bokeh-mid: #7a2418;
    --bokeh-deep: #3a0d08;
    --backdrop-dark: #0c0404;
    --fur-light: #9a8266;
    --fur-mid: #6e5a44;
  }
  * { margin: 0; padding: 0; box-sizing: border-box; }
  html, body {
    width: 1200px; height: 999px; overflow: hidden;
    background: var(--stage);
  }
  .cover-spread {
    position: absolute; left: 30px; top: 110px;
    width: 1148px; height: 802px;
    background: var(--paper);
  }
  .back-cover, .spine, .front-cover { position: absolute; }

  /* Back cover */
  .back-cover { left: 33px; top: 0; width: 500px; height: 802px; font-family: "PT Sans", sans-serif; }
  .back-heading {
    position: absolute; left: 4px;
    font-family: "PT Sans", sans-serif; font-weight: 700;
    font-size: 31px; letter-spacing: 0.6px; color: var(--brand-red); line-height: 1;
  }
  .summary-heading { top: 37px; }
  .author-heading { top: 523px; }
  .summary { position: absolute; left: 0; top: 86px; width: 499px; }
  .summary p, .author-bio {
    font-size: 16.2px; line-height: 20.2px; color: var(--body-ink);
    text-align: justify; text-align-last: left;
  }
  .summary p + p { margin-top: 13px; }
  .author-bio { position: absolute; left: 0; top: 570px; width: 329px; }
  .author-photo {
    position: absolute; left: 350px; top: 572px;
    width: 149px; height: 184px; border-radius: 16px;
    background: var(--ink);
  }

  /* Spine */
  .spine { left: 573px; top: 213px; width: 0; height: 376px; }
  .spine-title {
    position: absolute; left: 0; top: 0;
    width: 376px; transform-origin: 0 0;
    transform: translate(12px, 0) rotate(90deg);
    font-family: "Roboto Condensed", sans-serif; font-weight: 700;
    font-size: 24px; line-height: 1; white-space: nowrap;
    color: var(--brand-red); text-align: center;
  }

  /* Front cover */
  .front-cover { left: 592px; top: 0; width: 556px; height: 802px; }
  .front-title {
    position: absolute; left: 0; top: 26px; width: 556px;
    font-family: "Roboto Condensed", sans-serif; font-weight: 700;
    font-size: 72px; line-height: 1; color: var(--brand-red);
    text-align: center; letter-spacing: 0.5px;
  }
  .front-subtitle {
    position: absolute; left: 28px; top: 122px;
    font-family: "Roboto Condensed", sans-serif; font-weight: 700;
    font-size: 47px; line-height: 1; color: var(--ink);
  }
  .cover-art { position: absolute; left: 0; top: 80px; }
  .author-name {
    position: absolute; left: 0; top: 736px; width: 556px;
    font-family: "Roboto Condensed", sans-serif; font-weight: 700;
    font-size: 29px; line-height: 1; letter-spacing: 4.5px;
    color: var(--brand-red); text-align: center;
  }
</style>
</head>
<body>
  <main class="cover-spread">
    <section class="back-cover">
      <h2 class="back-heading summary-heading">Title Here</h2>
      <div class="summary">
        <p>Lorem ipsum dolor sit amet, consectetur adipiscing elit. Curabitur lacinia congue varius. Nunc ut augue cursus lectus aliquet elementum. Suspendisse semper sodales eros id cursus. Nunc lacinia adipiscing nibh. Maecenas eu dui velit. Sed nec sem leo. In a lacus scelerisque, condimentum turpis a, mollis orci. Integer nec orci justo. Nulla non dolor neque. Etiam condimentum erat sem, et posuere orci aliquam pellentesque. In nec ante quis urna gravida interdum. In lobortis elementum neque, nec interdum purus blandit sed. Curabitur adipiscing suscipit nunc ac molestie.</p>
        <p>Lorem ipsum dolor sit amet, consectetur adipiscing elit. Curabitur lacinia congue varius. Nunc ut augue cursus lectus aliquet elementum. Suspendisse semper sodales eros id cursus. Nunc lacinia adipiscing nibh. Maecenas eu dui velit. Sed nec sem leo. In a lacus scelerisque, condimentum turpis a, mollis orci. Integer nec orci justo. Nulla non dolor neque. Etiam condimentum erat sem, et posuere orci aliquam pellentesque. In nec ante quis urna gravida interdum. In lobortis elementum neque, nec interdum purus blandit sed. Curabitur adipiscing suscipit nunc ac molestie.</p>
      </div>
      <h2 class="back-heading author-heading">Author</h2>
      <p class="author-bio">Lorem ipsum dolor sit amet, consectetur adipiscing elit. Curabitur lacinia congue varius. Nunc ut augue cursus lectus aliquet elementum. Suspendisse semper sodales eros id cursus. Nunc lacinia adipiscing nibh. Maecenas eu dui velit. Sed nec sem leo. In a lacus scelerisque, condimentum turpis a, mollis orci. Integer nec orci justo. Nulla non dolor neque. Etiam condimentum erat sem, et</p>
      <div class="author-photo" role="img" aria-label="Author portrait placeholder"></div>
    </section>

    <aside class="spine">
      <div class="spine-title">Paper Lanterns - Borrowed Summers</div>
    </aside>

    <section class="front-cover">
      <h1 class="front-title">Paper Lanterns</h1>
      <p class="front-subtitle">Borrowed Summers</p>

      <svg class="cover-art" width="556" height="640" viewBox="0 0 556 640" xmlns="http://www.w3.org/2000/svg">
        <defs>
          <linearGradient id="backdropTone" x1="0" y1="0" x2="0" y2="1">
            <stop offset="0" stop-color="var(--bokeh-mid)"/>
            <stop offset="0.45" stop-color="var(--bokeh-deep)"/>
            <stop offset="0.72" stop-color="var(--bokeh-deep)"/>
            <stop offset="0.78" stop-color="var(--backdrop-dark)"/>
            <stop offset="1" stop-color="var(--backdrop-dark)"/>
          </linearGradient>
          <radialGradient id="warmGlowRight" cx="0.82" cy="0.42" r="0.45">
            <stop offset="0" stop-color="var(--bokeh-light)" stop-opacity="0.85"/>
            <stop offset="1" stop-color="var(--bokeh-light)" stop-opacity="0"/>
          </radialGradient>
          <radialGradient id="warmGlowLeft" cx="0.15" cy="0.45" r="0.4">
            <stop offset="0" stop-color="var(--bokeh-light)" stop-opacity="0.7"/>
            <stop offset="1" stop-color="var(--bokeh-light)" stop-opacity="0"/>
          </radialGradient>
          <radialGradient id="subjectTone" cx="0.5" cy="0.5" r="0.5">
            <stop offset="0" stop-color="var(--fur-light)"/>
            <stop offset="0.7" stop-color="var(--fur-mid)" stop-opacity="0.8"/>
            <stop offset="1" stop-color="var(--fur-mid)" stop-opacity="0"/>
          </radialGradient>
          <linearGradient id="swooshTop" x1="0" y1="0" x2="1" y2="0">
            <stop offset="0" stop-color="var(--swoosh-dark)"/>
            <stop offset="0.45" stop-color="var(--swoosh-red)"/>
            <stop offset="1" stop-color="var(--swoosh-red)"/>
          </linearGradient>
          <linearGradient id="swooshBottom" x1="0" y1="0" x2="1" y2="0">
            <stop offset="0" stop-color="var(--swoosh-red)"/>
            <stop offset="0.6" stop-color="var(--swoosh-red)"/>
            <stop offset="1" stop-color="var(--swoosh-dark)"/>
          </linearGradient>
          <clipPath id="photoFrame">
            <path d="M0,170 Q270,205 556,60 L556,585 Q290,612 0,540 Z"/>
          </clipPath>
        </defs>
        <g class="cover-photo" role="img" aria-label="Cover photograph: a large brown grizzly bear standing upright on its hind legs, set against a dark red backdrop of soft glowing bokeh lights" clip-path="url(#photoFrame)">
          <rect width="556" height="640" fill="url(#backdropTone)"/>
          <rect width="556" height="640" fill="url(#warmGlowRight)"/>
          <rect width="556" height="640" fill="url(#warmGlowLeft)"/>
          <ellipse cx="275" cy="430" rx="150" ry="250" fill="url(#subjectTone)"/>
        </g>
        <path class="swoosh swoosh-top" d="M0,135 Q280,195 556,0 L556,62 Q270,210 0,182 Z" fill="url(#swooshTop)"/>
        <path class="swoosh-highlight" d="M0,158 Q280,210 540,88" fill="none" stroke="var(--paper)" stroke-width="2" opacity="0.85"/>
        <path class="swoosh swoosh-bottom" d="M0,532 Q290,608 556,580 L520,592 Q270,640 0,590 Z" fill="url(#swooshBottom)"/>
        <path class="swoosh-highlight" d="M0,560 Q280,625 510,592" fill="none" stroke="var(--paper)" stroke-width="1.5" opacity="0.6"/>
      </svg>

      <p class="author-name">author name</p>
    </section>
  </main>
</body>
</html>
```